Money Mindset Podcast needs fun, creative cover art

Launching a new podcast called 'Turning the Page on Savings' - aimed at an audience 30-50 who are interested in the practicalities of managing their money but also the more mental and emotional aspects.
Looking for something not too serious, warm and friendly.

Must be easy to read on phone screens
3000 x 3000 in size
Avoid currency symbols $, £ etc, as may have an international audience

Target Market(s)

Podcast listeners age 30-50 starting in the UK but then worldwide. Probably 60:40 female bias

Industry/Entity Type

Life Coaching

Font styles to use
Serif
Sans Serif

Colors
cadf82
fee18a
acd037
85cae6
eea4c8
f59195
85acd3

Requirements
Must have
• Simple, clear design. Easy to read on variety of devices. 3000 x 3000
Appeal to those with a spiritual or emotional interests
Nice to have
• Stand out among other money related podcasts
Maybe play around with clouds, lightbulbs and clearing skies
Should not have
• Currency symbols such as $ or £
Be too corporate or bank like
Stock images

```html
<!DOCTYPE html>
<html lang="en">
<head>
<meta charset="utf-8">
<title>Turning the Page on Savings — Podcast Cover</title>
<link rel="stylesheet" href="https://fonts.googleapis.com/css2?family=Oswald:wght@600;700&display=swap">
<style>
  :root {
    --blue-deep: #0a2f66;
    --blue-mid: #1f5ca6;
    --blue-glow: #3d7cc4;
    --table-light: #e9e4da;
    --table-shade: #c9bfae;
    --title-white: #ffffff;
    --title-tan: #c7bb9c;
    --title-navy: #1c2b52;
  }
  html, body {
    margin: 0;
    padding: 0;
    width: 1200px;
    height: 1200px;
    overflow: hidden;
    background: var(--blue-deep);
  }
  .cover {
    position: relative;
    width: 1200px;
    height: 1200px;
    overflow: hidden;
  }
  .cover__photo {
    position: absolute;
    inset: 0;
    background:
      linear-gradient(180deg, rgba(0,0,0,0) 0%, rgba(0,0,0,0) 68%, var(--table-shade) 74%, var(--table-light) 84%, #d8d0c2 100%),
      radial-gradient(ellipse 70% 55% at 55% 45%, var(--blue-glow) 0%, var(--blue-mid) 45%, var(--blue-deep) 100%);
  }
  .cover__title {
    position: absolute;
    inset: 0;
    margin: 0;
    font-family: "Oswald", "Arial Narrow", sans-serif;
    font-weight: 700;
    text-transform: uppercase;
    letter-spacing: -2px;
  }
  .title-line {
    position: absolute;
    left: 330px;
    width: 840px;
    text-align: center;
    line-height: 1;
    white-space: nowrap;
  }
  .title-line--1 { top: 30px;  font-size: 232px; color: var(--title-white); }
  .title-line--2 { top: 255px; font-size: 232px; color: var(--title-white); }
  .title-line--3 { top: 480px; font-size: 232px; color: var(--title-tan); }
  .title-line--4 { top: 705px; font-size: 232px; color: var(--title-white); }
  .title-line--5 { top: 930px; font-size: 240px; color: var(--title-navy); }
</style>
</head>
<body>
  <main class="cover">
    <div class="cover__photo" role="img" aria-label="Photograph of stacked wooden letter dice on a pale wooden table against a deep blue backdrop"></div>
    <h1 class="cover__title">
      <span class="title-line title-line--1">Turning</span>
      <span class="title-line title-line--2">The</span>
      <span class="title-line title-line--3">Page</span>
      <span class="title-line title-line--4">On</span>
      <span class="title-line title-line--5">Savings</span>
    </h1>
  </main>
</body>
</html>
```